Name of Business is Tidewell Vitality Mentor,
Business Card and Logo Design for a health coaching practice that brings together all aspects of living including breathing, meditation, heartfelt intentional living, oneness with others, compassion, nutrition, hydration and primary care physician.

Target Market(s)

People looking for holistic approach to optimal living.

Industry/Entity Type

Business

Contact Information for Business Card

Marcus R.T. Dunmore
CLP, CCHC, C-IQ
Tidewell Vitality Mentor
614 Birchmoor Ave
Harbor Glen, MI 48390

Logo Text

Everything You Need Is Within You Now

```html
<!DOCTYPE html>
<html lang="en">
<head>
<meta charset="utf-8">
<title>Tidewell Vitality Mentor – Business Card</title>
<link rel="stylesheet" href="https://fonts.googleapis.com/css2?family=Source+Sans+3:wght@300;400;600;700&display=swap">
<style>
  :root {
    --bg: #ecebe8;
    --card-front: #f1f1f0;
    --card-back: #ffffff;
    --blue: #3d94d6;
    --blue-soft: #7bb8e6;
    --ink: #2f2f33;
    --ink-soft: #55565a;
    --shadow: 0 10px 28px rgba(0,0,0,.14), 0 2px 6px rgba(0,0,0,.08);
  }
  * { box-sizing: border-box; margin: 0; padding: 0; }
  html, body { width: 1200px; height: 800px; overflow: hidden; }
  body {
    background: var(--bg);
    font-family: "Source Sans 3", "Myriad Pro", Arial, sans-serif;
    display: flex; align-items: center; justify-content: center; gap: 40px;
  }
  .card {
    position: relative; width: 540px; height: 310px;
    border-radius: 16px; box-shadow: var(--shadow); overflow: hidden;
  }

  /* Front */
  .card--front { background: var(--card-front); }
  .brand { position: absolute; display: flex; align-items: center; gap: 12px; }
  .brand__dot { width: 26px; height: 26px; border-radius: 50%; background: var(--blue); flex: none; }
  .brand__name { font-weight: 600; color: var(--blue); line-height: 1; white-space: nowrap; }
  .card--front .brand { left: 50%; top: 78px; transform: translateX(-50%); }
  .card--front .brand__name { font-size: 34px; }
  .pillars {
    position: absolute; left: 0; right: 0; top: 160px;
    text-align: center; color: var(--blue); font-size: 15px; font-weight: 600; line-height: 1.45;
  }

  /* Back */
  .card--back { background: var(--card-back); }
  .card--back .brand { right: 34px; top: 30px; gap: 8px; }
  .card--back .brand__dot { width: 14px; height: 14px; }
  .card--back .brand__name { font-size: 17px; }
  .holder { position: absolute; left: 30px; top: 104px; padding-left: 16px; }
  .holder::before {
    content: ""; position: absolute; left: 0; top: 4px; width: 6px; height: 44px; background: var(--blue);
  }
  .holder__name { font-size: 25px; color: var(--ink); font-weight: 300; line-height: 1.1; }
  .holder__name strong { font-weight: 700; }
  .holder__creds { font-size: 15px; color: var(--blue); margin-top: 3px; letter-spacing: .3px; }
  .contact { position: absolute; left: 30px; top: 180px; list-style: none; }
  .contact li { display: flex; align-items: flex-start; gap: 12px; font-size: 13.5px; color: var(--ink-soft); line-height: 1.3; margin-bottom: 6px; }
  .contact svg { flex: none; width: 18px; height: 18px; margin-top: 1px; }
  .rule { position: absolute; left: 0; bottom: 27px; width: 330px; height: 2px; background: var(--blue); }
  .site { position: absolute; right: 30px; bottom: 20px; font-size: 14px; color: var(--blue); line-height: 1; }
</style>
</head>
<body>
  <section class="card card--front" aria-label="Card front">
    <div class="brand">
      <span class="brand__dot"></span>
      <span class="brand__name">Tidewell Vitality Mentor</span>
    </div>
    <p class="pillars">
      Breathing | Rest | Meditation | Heartfelt Living | Movement<br>
      Oneness | Nutrition | Water<br>
      See Your Dr. Regularly
    </p>
  </section>

  <section class="card card--back" aria-label="Card back">
    <div class="brand">
      <span class="brand__dot"></span>
      <span class="brand__name">Tidewell Vitality Mentor</span>
    </div>
    <div class="holder">
      <h1 class="holder__name">Marcus <strong>R.T. Dunmore</strong></h1>
      <p class="holder__creds">CLP, CCHC, C-IQ</p>
    </div>
    <ul class="contact">
      <li>
        <svg viewBox="0 0 18 18" aria-hidden="true"><circle cx="9" cy="9" r="8" fill="none" stroke="var(--blue-soft)"/><path d="M9 4.5a3 3 0 0 0-3 3c0 2.2 3 5.5 3 5.5s3-3.3 3-5.5a3 3 0 0 0-3-3z" fill="var(--blue)"/><circle cx="9" cy="7.5" r="1" fill="#fff"/></svg>
        <span>614 Birchmoor Ave<br>Harbor Glen, MI 48390</span>
      </li>
      <li>
        <svg viewBox="0 0 18 18" aria-hidden="true"><circle cx="9" cy="9" r="8" fill="none" stroke="var(--blue-soft)"/><path d="M6.3 5h1.6l.8 2-1 .8a5 5 0 0 0 2.5 2.5l.8-1 2 .8v1.6c0 .5-.4.8-.9.8A7 7 0 0 1 5.5 5.9c0-.5.3-.9.8-.9z" fill="var(--blue)"/></svg>
        <span>000 000 0000</span>
      </li>
      <li>
        <svg viewBox="0 0 18 18" aria-hidden="true"><circle cx="9" cy="9" r="8" fill="none" stroke="var(--blue-soft)"/><rect x="5" y="6" width="8" height="6" rx="1" fill="var(--blue)"/><path d="M5.3 6.4 9 9.2l3.7-2.8" fill="none" stroke="#fff" stroke-width=".9"/></svg>
        <span>hello@tidewellmentor.com</span>
      </li>
    </ul>
    <span class="rule"></span>
    <span class="site">www.tidewellmentor.com</span>
  </section>
</body>
</html>
```